Business Cards- The Manor at Brookridge Golf Club

We would like our business cards to look more high-end. We are a wedding venue that has been in business for 60+ years. We like our logo and our colors - primarily green and a touch of gold/beige. The owner wants our business cards to look more special..

Target Market(s)

Brides who have already toured our venue

Industry/Entity Type

Wedding venue - mansion

Contact Information for Business Card

Name, email, physical address, phone number

Colors
00AB8E
00BBA5
67D7C9
C6EFE9
E9F9F6

Requirements
Must have
• I think we would like our cards to be so pretty that people will want to keep them and will remember the venue. The venue is historic (built in 1850) and beautiful.
Nice to have
• Could we put an image of the building on one side and the contact info on the other?
Should not have
• The color black

```html
<!DOCTYPE html>
<html lang="en">
<head>
<meta charset="UTF-8">
<title>The Manor at Brookridge Golf Club – Business Card</title>
<link href="https://fonts.googleapis.com/css2?family=Montserrat:wght@400;500;700&display=swap" rel="stylesheet">
<style>
  :root {
    --bg: #d9d9d9;
    --card: #ffffff;
    --green: #6c9a3c;
    --beige: #c4aa86;
    --ink: #4a4d4f;
    --sky-top: #2f6fd1;
    --sky-low: #7fb2ec;
    --trees: #1f3a25;
    --lawn: #5b8a3a;
    --chairs: #e6e6e1;
  }
  * { margin: 0; padding: 0; box-sizing: border-box; }
  html, body { width: 1200px; height: 900px; overflow: hidden; }
  body {
    background: var(--bg);
    font-family: "Montserrat", Arial, sans-serif;
    position: relative;
  }
  .card {
    position: absolute;
    left: 250px;
    width: 700px;
    height: 400px;
    border-radius: 34px;
    overflow: hidden;
    background: var(--card);
  }
  .card-front { top: 40px; }
  .card-back { top: 460px; }

  .venue-photo {
    position: absolute;
    inset: 0;
    background:
      linear-gradient(180deg,
        var(--sky-top) 0%,
        var(--sky-low) 30%,
        var(--trees) 42%,
        var(--trees) 70%,
        var(--lawn) 78%,
        var(--chairs) 88%,
        var(--lawn) 100%);
  }
  .front-brand {
    position: absolute;
    right: 40px;
    top: 150px;
    display: flex;
    align-items: center;
    gap: 10px;
    color: var(--green);
    font-weight: 700;
    font-size: 26px;
    line-height: 1.15;
    white-space: nowrap;
  }
  .brand-dot {
    width: 16px; height: 16px;
    border-radius: 50%;
    background: var(--beige);
    flex: none;
  }

  .back-brand {
    position: absolute;
    left: 60px;
    top: 80px;
    display: flex;
    align-items: center;
    gap: 14px;
    color: var(--green);
    font-weight: 700;
    font-size: 34px;
    line-height: 1.15;
    white-space: nowrap;
  }
  .back-brand .brand-dot { width: 22px; height: 22px; }

  .person { position: absolute; left: 60px; top: 222px; }
  .person-name {
    color: var(--green);
    font-weight: 700;
    font-size: 26px;
    letter-spacing: 0.5px;
    text-transform: uppercase;
  }
  .person-title {
    color: var(--beige);
    font-size: 18px;
    margin-top: 2px;
  }
  .contact-list {
    list-style: none;
    position: absolute;
    left: 60px;
    top: 300px;
    color: var(--ink);
    font-size: 17px;
  }
  .contact-list li {
    display: flex;
    align-items: center;
    gap: 12px;
    height: 26px;
  }
  .contact-list svg { width: 18px; height: 18px; fill: var(--green); flex: none; }

  .address {
    position: absolute;
    right: 50px;
    top: 250px;
    text-align: right;
    color: var(--ink);
    font-size: 17px;
    line-height: 1.45;
  }
</style>
</head>
<body>

  <section class="card card-front">
    <div class="venue-photo" role="img" aria-label="Photo of the outdoor ceremony lawn: tall evergreen hedge under a blue sky, wedding arbor and rows of white chairs"></div>
    <div class="front-brand">
      <span class="brand-dot"></span>
      <span>The Manor<br>at Brookridge Golf Club</span>
    </div>
  </section>

  <section class="card card-back">
    <div class="back-brand">
      <span class="brand-dot"></span>
      <span>The Manor<br>at Brookridge Golf Club</span>
    </div>

    <div class="person">
      <div class="person-name">Daniel Hart</div>
      <div class="person-title">Managing Director</div>
    </div>

    <ul class="contact-list">
      <li>
        <svg viewBox="0 0 24 24" aria-hidden="true"><path d="M6.6 10.8a15.1 15.1 0 0 0 6.6 6.6l2.2-2.2a1 1 0 0 1 1-.25 11.4 11.4 0 0 0 3.6.57 1 1 0 0 1 1 1V20a1 1 0 0 1-1 1A17 17 0 0 1 3 4a1 1 0 0 1 1-1h3.5a1 1 0 0 1 1 1c0 1.25.2 2.45.57 3.57a1 1 0 0 1-.25 1z"/></svg>
        044-555 018 274
      </li>
      <li>
        <svg viewBox="0 0 24 24" aria-hidden="true"><path d="M2 5h20v14H2z M3.5 6.5 12 13l8.5-6.5" fill="none" stroke="#6c9a3c" stroke-width="2"/></svg>
        events@brookridgemanor.com
      </li>
      <li>
        <svg viewBox="0 0 24 24" aria-hidden="true"><g fill="none" stroke="#6c9a3c" stroke-width="2"><circle cx="12" cy="12" r="9"/><path d="M3 12h18M12 3c3 3 3 15 0 18M12 3c-3 3-3 15 0 18"/></g></svg>
        www.brookridgemanor.com
      </li>
    </ul>

    <div class="address">
      88 Orchard Hill Road<br>
      60318, Fairview
    </div>
  </section>

</body>
</html>
```